Bed and Breakfast WebSite Design

We need a webdesign for a bed and breakfast in Germany. This house is located at the scenic river Mosel in Germany, a very small town called Piesport. It's a region known for its wines. A lot of nature, bicycle routes, hiking, boat tours...

The house itself is a former monastery and because of that a listed, historic buildung.
The house is entirely renewed and has a very modern, individual interieur with "boutique hotel" style rooms. Every room is different. Its family owned and operated.

The website should find a bridge between historic charme and modern individual friendlyness. Very straight, not fancy. The website should express familiy friendlyness, modern comfort and emphasize that its place to RELAX.

In the attachment you'll find a lot of photos of house and surrounding. Theres a separate zip with lumetra stockphotos of that particular location/town (not purchased yet).

Number of Pages Required

1 page

Requirements
Must have
• Should be "easily" made responsive.

```html
<!DOCTYPE html>
<html lang="de">
<head>
<meta charset="utf-8">
<title>Rebenhaus Piesport</title>
<link href="https://fonts.googleapis.com/css2?family=Libre+Baskerville:wght@400;700&family=Poppins:wght@300;400;500&display=swap" rel="stylesheet">
<style>
:root{
  --green:#86a33a;
  --green-dark:#6f8a2a;
  --ink:#2b2b2b;
  --muted:#8a8a8a;
  --soft:#f3f3f3;
  --white:#ffffff;
  --rule:#c9d3a6;
  --map:#e9dcb4;
  --serif:'Libre Baskerville', Georgia, serif;
  --sans:'Poppins', Arial, sans-serif;
}
*{margin:0;padding:0;box-sizing:border-box}
html,body{width:1200px;height:5391px;overflow:hidden}
body{font-family:var(--sans);color:var(--ink);background:var(--white)}
section,header,footer{position:relative;width:1200px;overflow:hidden}
.abs{position:absolute}
.photo{position:absolute;display:block}
.label{position:absolute;font-family:var(--sans);font-size:10px;letter-spacing:2.5px;color:var(--green);text-transform:uppercase}
.title{position:absolute;font-family:var(--serif);font-weight:400;font-size:38px;letter-spacing:3px;color:var(--ink);line-height:1.45}
.title strong{font-weight:700}
.title .accent{color:var(--green);font-weight:700}
.copy{position:absolute;font-size:9.5px;line-height:2;color:var(--muted)}
.center{left:0;width:1200px;text-align:center}

/* nav */
.site-nav{height:59px;background:var(--white)}
.brand{left:88px;top:20px;font-family:var(--serif);font-size:15px;color:var(--green)}
.nav-link{top:24px;font-size:10px;letter-spacing:.5px;color:var(--ink)}
.nav-link.active{color:var(--green);text-decoration:underline}
.book-btn{left:949px;top:16px;width:109px;height:28px;background:var(--green);color:var(--white);font-size:10px;letter-spacing:1px;display:flex;align-items:center;justify-content:center}
.lang-btn{left:1078px;top:16px;width:34px;height:28px;border:1px solid #bbb;font-size:10px;color:var(--green);display:flex;align-items:center;justify-content:center}

/* hero */
.hero{height:575px;background:#0e1630}
.hero-photo{inset:0;background:radial-gradient(ellipse at 60% 70%,#a2782c 0%,#4a3a24 30%,transparent 60%),linear-gradient(180deg,#1b2b6a 0%,#14204a 45%,#1e1a12 100%)}
.hero-title{top:166px;font-family:var(--serif);font-size:38px;letter-spacing:5px;color:var(--white);font-weight:700}
.hero-sub{top:228px;font-size:20px;font-weight:300;color:var(--white)}
.hero-btn{left:505px;top:278px;width:190px;height:32px;background:var(--green);color:var(--white);font-size:12px;letter-spacing:1.5px;display:flex;align-items:center;justify-content:center;gap:10px}
.scroll-hint{top:488px;font-family:var(--serif);font-size:11px;letter-spacing:1px;color:var(--white)}
.slider-dot{top:528px;width:6px;height:6px;border-radius:50%;background:var(--white)}
.slider-dot.current{width:20px;height:20px;top:521px;border:2px solid var(--white);background:transparent}
.slider-dot.current::after{content:"";position:absolute;left:5px;top:5px;width:6px;height:6px;border-radius:50%;background:var(--white)}

/* story */
.story{height:816px;background:var(--soft)}
.since{left:644px;top:660px;font-family:var(--serif);font-size:68px;letter-spacing:11px;color:#c9c9c9;font-weight:700}

/* accommodation */
.living{height:702px;background:var(--white)}
.living-rule{left:173px;top:0;width:2px;height:306px;background:#444}
.room-card{position:absolute;top:362px}
.room-caption{position:absolute;font-family:var(--serif);font-size:15px;letter-spacing:1.5px;color:var(--ink)}
.room-card.featured{background:var(--soft)}
.view-more{position:absolute;font-size:9px;color:var(--green)}

/* gallery */
.gallery{height:776px;background:var(--soft)}

/* dining & things */
.dining{height:626px;background:var(--white)}
.things{height:628px;background:var(--soft)}
.feature-head{position:absolute;font-family:var(--serif);font-size:12px;letter-spacing:1.5px;color:var(--green);display:flex;align-items:center;gap:12px}
.feature-rule{position:absolute;height:1px;background:var(--rule)}
.feature-item{position:absolute;font-family:var(--serif);font-size:12px;letter-spacing:1.5px;color:#444;display:flex;align-items:center;gap:14px}
.diamond{width:8px;height:8px;background:#333;transform:rotate(45deg);display:inline-block}
.diamond.green{background:var(--green)}

/* location */
.location{height:482px;background:var(--white)}
.loc-tag{left:209px;top:244px;font-size:10px;letter-spacing:2.5px;color:var(--ink)}
.loc-rule{left:209px;top:279px;width:279px;height:1px;background:var(--rule)}
.loc-text{left:209px;font-family:var(--serif);font-size:11px;letter-spacing:2px;color:#444}

/* strip */
.strip{height:332px;background:var(--soft)}

/* footer */
.site-footer{height:395px;background:linear-gradient(180deg,#f0f0ef 0%,#b9bcba 30%,#6d706c 60%,#3a3c38 100%)}
.signup-label{top:40px;font-size:10px;letter-spacing:2.5px;color:#e9e9e9}
.signup{left:446px;top:82px;width:306px;height:43px;background:var(--white);display:flex;align-items:center;padding-left:16px;font-size:10px;color:#999;letter-spacing:1px}
.signup-btn{position:absolute;right:6px;top:6px;width:32px;height:31px;background:var(--green);color:var(--white);font-size:9px;display:flex;align-items:center;justify-content:center}
.foot-nav{top:174px;font-size:9px;color:#eee;display:flex;justify-content:center;gap:38px}
.foot-rule{left:216px;top:218px;width:900px;height:1px;background:#8e918d}
.foot-head{font-family:var(--serif);font-size:10px;letter-spacing:1.5px;color:#ddd}
.foot-text{font-size:10px;color:#eee;line-height:1.6}
.social-dot{display:inline-block;width:11px;height:11px;border-radius:50%;background:#eee;margin-right:9px}
.contact-row{position:absolute;left:846px;display:flex;align-items:center;gap:12px;font-size:10px;color:#fff;letter-spacing:.5px}
.copyright{top:360px;font-size:8px;color:#ccc;letter-spacing:1px}
</style>
</head>
<body>

<header class="site-nav">
  <div class="abs brand">Rebenhaus Piesport</div>
  <span class="abs nav-link active" style="left:418px">HOME</span>
  <span class="abs nav-link" style="left:490px">ABOUT</span>
  <span class="abs nav-link" style="left:585px">THINGS TO DO</span>
  <span class="abs nav-link" style="left:686px">LOCATION</span>
  <span class="abs nav-link" style="left:774px">GALLERY</span>
  <div class="abs book-btn">BOOK NOW</div>
  <div class="abs lang-btn">En</div>
</header>

<section class="hero">
  <div class="photo hero-photo" role="img" aria-label="Evening terrace of the guesthouse with string lights, parasol, tables and chairs"></div>
  <div class="abs center hero-title">Rebenhaus</div>
  <div class="abs center hero-sub">Herzlich willkommen im Rebenhaus in Piesport</div>
  <div class="abs hero-btn">EXPLORE NOW
    <svg width="14" height="10" viewBox="0 0 14 10"><path d="M0 5h12M8 1l4 4-4 4" stroke="#fff" fill="none" stroke-width="1.4"/></svg>
  </div>
  <div class="abs center scroll-hint">scroll down</div>
  <svg class="abs" style="left:592px;top:516px" width="16" height="26" viewBox="0 0 16 26"><rect x="1" y="1" width="14" height="24" rx="7" stroke="#fff" fill="none" stroke-width="1.4"/><line x1="8" y1="6" x2="8" y2="11" stroke="#fff" stroke-width="1.6"/></svg>
  <span class="abs slider-dot" style="left:97px"></span>
  <span class="abs slider-dot current" style="left:123px"></span>
  <span class="abs slider-dot" style="left:163px"></span>
  <span class="abs slider-dot" style="left:196px"></span>
</section>

<section class="story">
  <div class="label" style="left:173px;top:74px">The Story</div>
  <h2 class="title" style="left:173px;top:110px">The Tradition of<br><strong>Hospitality</strong></h2>
  <div class="abs" style="left:173px;top:260px;width:77px;height:1px;background:#555"></div>
  <p class="copy" style="left:277px;top:248px;width:300px">Fühlen Sie sich zu Hause und genießen Sie die private Atmosphäre unseres Hauses, den Garten, den Blick auf die Weinberge und die Mosel!</p>
  <p class="copy" style="left:709px;top:248px;width:360px">Gastfreundschaft hat in unserer Familie eine lange Tradition, die wir gerne fortführen. Unser Haus ist denkmalgeschützter Teil eines alten Klostergutes und diesen Charme möchten wir erhalten und beleben.</p>
  <div class="photo" style="left:88px;top:361px;width:259px;height:121px;background:linear-gradient(160deg,#7fa35a,#3f5a2a)" role="img" aria-label="Garden with parasol overlooking vineyards"></div>
  <div class="photo" style="left:374px;top:361px;width:232px;height:121px;background:linear-gradient(160deg,#3a2418,#a6643a)" role="img" aria-label="Candlelit dinner table in the vaulted cellar"></div>
  <div class="photo" style="left:632px;top:361px;width:178px;height:148px;background:linear-gradient(160deg,#8fb06a,#56703a)" role="img" aria-label="Lawn and terrace of the house in summer"></div>
  <div class="photo" style="left:837px;top:361px;width:223px;height:148px;background:linear-gradient(160deg,#c9b9a4,#6e5a48)" role="img" aria-label="Breakfast room with tables and windows"></div>
  <div class="photo" style="left:151px;top:505px;width:182px;height:150px;background:linear-gradient(180deg,#7ea9d6,#4e6e3a 60%,#2e4a5a)" role="img" aria-label="Historic half-timbered house seen from the river"></div>
  <div class="photo" style="left:360px;top:505px;width:259px;height:150px;background:linear-gradient(160deg,#1e140e,#8a4a22)" role="img" aria-label="Candles and wine glasses in the cellar"></div>
  <div class="photo" style="left:644px;top:535px;width:185px;height:120px;background:linear-gradient(180deg,#7faee0,#5f8a3e)" role="img" aria-label="House facade behind trees"></div>
  <div class="photo" style="left:853px;top:505px;width:261px;height:150px;background:linear-gradient(160deg,#8aa65c,#7a4a30)" role="img" aria-label="Rusted garden gate in front of greenery"></div>
  <div class="since">Since 1990</div>
</section>

<section class="living">
  <div class="abs living-rule"></div>
  <div class="label" style="left:216px;top:76px">The Living</div>
  <h2 class="title" style="left:216px;top:108px">Accommodation</h2>
  <p class="copy" style="left:216px;top:195px;width:405px">Seitwärts der Mosel bieten wir Ihnen viele schöne Plätze zum Entspannen, ausspannen, lesen oder gesellig sein. Unser hauseigener Bootsanleger bietet gute Bedingungen für Wassersportler und einen Logenplatz auf dem Wasser. Der Radweg führt direkt am Haus vorbei, die Mosel bietet schöne Ziele für Radwanderer und wunderbare Entdeckungen.</p>
  <p class="copy" style="left:657px;top:195px;width:405px">Zahlreiche Wanderwege und Ausflugsziele in der näheren Umgebung bieten Ihnen einen abwechslungsreichen Aufenthalt. Die hervorragenden Piesporter Weine und die feine regionale Küche können Sie in Piesport auf jedem Niveau genießen – von der familiären Winzerstube bis zum feinen Restaurant.</p>
  <div class="room-card" style="left:216px;width:277px">
    <div class="photo" style="position:relative;width:277px;height:154px;background:linear-gradient(160deg,#6f9a4a,#3e5a2a)" role="img" aria-label="Historic building among trees"></div>
    <div class="room-caption" style="left:18px;top:176px">Historic Building</div>
  </div>
  <div class="room-card featured" style="left:504px;width:277px;height:277px">
    <div class="photo" style="position:relative;width:277px;height:194px;background:linear-gradient(160deg,#d8cfc4,#6b5748)" role="img" aria-label="Modern guest room with double bed"></div>
    <div class="room-caption" style="left:18px;top:218px">Individual Interieur</div>
    <div class="view-more" style="left:18px;top:250px">View more »</div>
  </div>
  <div class="room-card" style="left:794px;width:275px">
    <div class="photo" style="position:relative;width:275px;height:154px;background:linear-gradient(180deg,#8fb4dc,#5f7f4a 55%,#4a6a8a)" role="img" aria-label="River bend with vineyards and town"></div>
    <div class="room-caption" style="left:18px;top:176px">A Lot Of Nature</div>
  </div>
</section>

<section class="gallery">
  <div class="label" style="left:216px;top:76px">The Gallery</div>
  <h2 class="title" style="left:216px;top:112px">The Glimpse To<br><span class="accent">Boutique Hotel</span></h2>
  <div class="photo" style="left:216px;top:260px;width:259px;height:110px;background:linear-gradient(160deg,#7fa35a,#3f5a2a)" role="img" aria-label="Garden with parasol"></div>
  <div class="photo" style="left:502px;top:260px;width:234px;height:110px;background:linear-gradient(160deg,#3a2418,#a6643a)" role="img" aria-label="Candlelit cellar table"></div>
  <div class="photo" style="left:760px;top:260px;width:178px;height:134px;background:linear-gradient(160deg,#8fb06a,#56703a)" role="img" aria-label="Lawn and terrace"></div>
  <div class="photo" style="left:965px;top:260px;width:223px;height:134px;background:linear-gradient(160deg,#c9b9a4,#6e5a48)" role="img" aria-label="Breakfast room"></div>
  <div class="photo" style="left:128px;top:394px;width:259px;height:137px;background:linear-gradient(160deg,#1e140e,#8a4a22)" role="img" aria-label="Candles in the cellar"></div>
  <div class="photo" style="left:421px;top:394px;width:319px;height:137px;background:linear-gradient(160deg,#8aa65c,#7a4a30)" role="img" aria-label="Rusted garden gate"></div>
  <div class="photo" style="left:772px;top:420px;width:184px;height:111px;background:linear-gradient(180deg,#7faee0,#5f8a3e)" role="img" aria-label="House facade behind trees"></div>
  <div class="photo" style="left:983px;top:394px;width:217px;height:137px;background:linear-gradient(160deg,#8aa65c,#7a4a30)" role="img" aria-label="Garden gate detail"></div>
  <div class="photo" style="left:216px;top:558px;width:259px;height:137px;background:linear-gradient(160deg,#7fa35a,#3f5a2a)" role="img" aria-label="Garden with parasol"></div>
  <div class="photo" style="left:502px;top:558px;width:180px;height:137px;background:linear-gradient(180deg,#7ea9d6,#4e6e3a 60%,#2e4a5a)" role="img" aria-label="House seen from the river"></div>
  <div class="photo" style="left:718px;top:558px;width:178px;height:137px;background:linear-gradient(160deg,#8fb06a,#56703a)" role="img" aria-label="Lawn and terrace"></div>
  <div class="photo" style="left:922px;top:558px;width:221px;height:137px;background:linear-gradient(160deg,#c9b9a4,#6e5a48)" role="img" aria-label="Breakfast room"></div>
</section>

<section class="dining">
  <div class="label center" style="top:76px">The Dining</div>
  <h2 class="title center" style="top:108px">Exquisitely Crafted<br><span class="accent">Dining Moments</span></h2>
  <div class="feature-head" style="left:231px;top:262px"><span class="diamond green"></span>NIGHT LIFE</div>
  <div class="feature-rule" style="left:231px;top:302px;width:420px"></div>
  <p class="copy" style="left:253px;top:325px;width:240px">Lorem ipsum dolor sit amet, consetetur sadipscing elitr, sed diam nonumy eirmod tempor invidunt ut labore et dolore magna aliquyam erat, sed diam voluptua. At vero eos</p>
  <div class="feature-item" style="left:231px;top:426px"><span class="diamond"></span>CANDLE LIGHT DINNER</div>
  <div class="feature-item" style="left:231px;top:464px"><span class="diamond"></span>FOOD AND BEVERAGES</div>
  <div class="feature-item" style="left:231px;top:502px"><span class="diamond"></span>DRINK &amp; CHILL</div>
  <div class="photo" style="left:600px;top:260px;width:472px;height:292px;background:radial-gradient(ellipse at 50% 70%,#c7752e,#4a2410 55%,#1c0f08)" role="img" aria-label="Guests enjoying wine by candlelight in the vaulted cellar"></div>
</section>

<section class="things">
  <div class="label center" style="top:78px">Things To Do</div>
  <h2 class="title center" style="top:112px">Exquisitely Crafted<br><span class="accent">Magic Moments</span></h2>
  <div class="photo" style="left:231px;top:268px;width:472px;height:290px;background:linear-gradient(180deg,#6fa0d8 0%,#4e7a3a 35%,#3e5a2a 60%,#24507a 75%,#1a3a5a)" role="img" aria-label="Boat dock on the river in front of the historic house"></div>
  <div class="feature-head" style="left:815px;top:268px"><span class="diamond green"></span>BOAT TOURS</div>
  <div class="feature-rule" style="left:815px;top:307px;width:256px"></div>
  <p class="copy" style="left:837px;top:330px;width:240px">Lorem ipsum dolor sit amet, consetetur sadipscing elitr, sed diam nonumy eirmod tempor invidunt ut labore et dolore magna aliquyam erat, sed diam voluptua. At vero eos</p>
  <div class="feature-item" style="left:815px;top:435px"><span class="diamond"></span>BICYCLE ROUTES</div>
  <div class="feature-item" style="left:815px;top:473px"><span class="diamond"></span>HIKING</div>
  <div class="feature-item" style="left:815px;top:511px"><span class="diamond"></span>WINES</div>
</section>

<section class="location">
  <div class="label" style="left:209px;top:76px">The Location</div>
  <h2 class="title" style="left:209px;top:110px">Where<br><span class="accent">We Are..</span></h2>
  <div class="abs loc-tag">SCENIC RIVER MOSEL IN GERMANY</div>
  <div class="abs loc-rule"></div>
  <div class="abs loc-text" style="top:304px">Wir Freuen Uns, Sie Als Gäste Im<br>Rebenhaus Begrüßen Zu Dürfen.</div>
  <div class="abs loc-text" style="top:352px">Herzlichst<br><strong>Ihre Familie Hartmann</strong></div>
  <div class="photo" style="left:727px;top:74px;width:281px;height:328px;background:radial-gradient(ellipse at 50% 50%,var(--map) 60%,#f6f0dd 100%);border-radius:40% 45% 35% 40%" role="img" aria-label="Map of Germany with the Mosel region highlighted"></div>
</section>

<section class="strip">
  <div class="label center" style="top:82px">The Gallery</div>
  <div class="photo" style="left:88px;top:127px;width:171px;height:158px;background:linear-gradient(160deg,#e6e1da,#8a7a6a)" role="img" aria-label="Bathroom with sink"></div>
  <div class="photo" style="left:259px;top:127px;width:171px;height:158px;background:linear-gradient(160deg,#7a9a4a,#4a5a3a)" role="img" aria-label="Garden path to the house"></div>
  <div class="photo" style="left:430px;top:127px;width:171px;height:158px;background:linear-gradient(180deg,#8ab4de,#6a8a4a 55%,#7a5a3a)" role="img" aria-label="Wooden jetty in front of the house"></div>
  <div class="photo" style="left:601px;top:127px;width:171px;height:158px;background:linear-gradient(180deg,#9ac0e6,#6a9a4a)" role="img" aria-label="Vineyard slopes"></div>
  <div class="photo" style="left:772px;top:127px;width:171px;height:158px;background:linear-gradient(160deg,#6a8a3a,#3a4a2a)" role="img" aria-label="Garden gate with greenery"></div>
  <div class="photo" style="left:943px;top:127px;width:171px;height:158px;background:linear-gradient(160deg,#a6b48a,#e8e4dc)" role="img" aria-label="Guest room with patterned wallpaper"></div>
</section>

<footer class="site-footer">
  <div class="abs center signup-label">SIGN UP FOR UPDATES</div>
  <div class="abs signup">enter your email address<span class="signup-btn">GO</span></div>
  <nav class="abs center foot-nav"><span>HOME</span><span>ABOUT</span><span>THINGS TO DO</span><span>LOCATION</span><span>GALLERY</span></nav>
  <div class="abs foot-rule"></div>
  <div class="abs" style="left:216px;top:249px">
    <div class="foot-head">CONNECT WITH US</div>
    <div style="margin-top:12px"><span class="social-dot"></span><span class="social-dot"></span><span class="social-dot"></span><span class="social-dot"></span><span class="social-dot"></span></div>
  </div>
  <div class="abs" style="left:479px;top:249px">
    <div class="foot-head">CONTACT US</div>
    <div class="foot-text" style="margin-top:10px">Rebenhaus Piesport Inh. Greta Hartmann<br>Am Rebhang 12</div>
  </div>
  <div class="contact-row" style="top:236px">
    <svg width="12" height="16" viewBox="0 0 12 16"><rect x="1" y="1" width="10" height="14" rx="2" fill="none" stroke="#fff" stroke-width="1.3"/><circle cx="6" cy="12.5" r="1" fill="#fff"/></svg>
    +49(0)6500 - 12 34 560</div>
  <div class="contact-row" style="top:264px">
    <svg width="14" height="14" viewBox="0 0 14 14"><path d="M3 1l3 3-2 2c1 2 2 3 4 4l2-2 3 3-2 2C6 13 1 8 1 3z" fill="#fff"/></svg>
    +49(0)150 - 000 12 345</div>
  <div class="contact-row" style="top:290px">
    <svg width="14" height="10" viewBox="0 0 14 10"><rect x=".7" y=".7" width="12.6" height="8.6" fill="none" stroke="#fff" stroke-width="1.3"/><path d="M1 1l6 5 6-5" fill="none" stroke="#fff" stroke-width="1.3"/></svg>
    INFO@REBENHAUS-MAIL.DE</div>
  <div class="abs center copyright">© COPYRIGHT 2020 | REBENHAUS</div>
</footer>

</body>
</html>
```